Brisk Lyceum Website

We are looking for a new design of our website. The current website is www.brisklyceum-example.com. The company is the #1 pre-college math and science program in Orange County, CA. We would like to see designs that integrate our logo with a modern color scheme. We are also open for suggestions that could improve our logo. We would like a simple, minimal, clean, classy, and vibrant front-page user interface design that give the premium, modern, innovative, creative, and premier brand feel. We like the "New Retro Colors for the Web" as described here: http://www.pixelharbor-example.net/en/layout-notes-2013/.

Target Market(s)

The target market is parents with K-12 students from a diverse population. Parents are well educated with family income > $150,000. Most of the decision makers are mothers from immigrate families: 30% Chinese, 30% Korean, 15% Indian, 24% White.

Industry/Entity Type

College

Requirements
Must have
• Must read our statement of differentiation at:
• http://brisklyceum-example.com/about-us
• Your design must be reflective of your understanding of the statements.
Nice to have
• The design should also be mobil friendly.
Should not have
• While most of our current classes are math, our company is expanding to include STEM (Science, Technology, Engineering, and Math) for gifted students. Therefore, the site should not be JUST a math education site.

```html
<!DOCTYPE html>
<html lang="en">
<head>
<meta charset="utf-8">
<title>Brisk Lyceum for Gifted Youth</title>
<link rel="stylesheet" href="https://fonts.googleapis.com/css2?family=Mulish:wght@400;600&family=Source+Sans+3:ital,wght@0,400;1,400&display=swap">
<style>
:root{
  --page:#eceeed;
  --white:#ffffff;
  --ink:#3a3a3a;
  --brand:#34376e;
  --muted:#9a9a9a;
  --green:#8dc63f;
  --yellow:#ebb622;
  --gold-link:#e0a815;
  --red:#f0565a;
  --teal:#28b4c3;
  --field:#f0f1f1;
}
*{box-sizing:border-box;margin:0;padding:0}
html,body{width:1056px;height:1200px;overflow:hidden}
body{background:var(--page);font-family:"Source Sans 3",sans-serif;color:var(--ink);position:relative}
a{text-decoration:none}
.display{font-family:"Mulish",sans-serif}

.site-header{position:absolute;left:0;top:0;width:1056px;height:108px;background:linear-gradient(#ffffff,#f1f2f2)}
.brand{position:absolute;left:88px;top:36px;display:flex;align-items:center;gap:12px}
.brand-mark{width:34px;height:34px;border-radius:50%;background:var(--green)}
.brand-name{font-family:"Mulish",sans-serif;font-size:28px;font-weight:400;color:var(--brand);line-height:1}
.login{position:absolute;left:776px;top:11px;font-size:11px;color:#222;text-decoration:underline}
.search{position:absolute;left:819px;top:9px;width:140px;height:19px;border:1px solid #c9cccc;background:#fff;display:flex}
.search-drop{width:15px;border-right:1px solid #d5d8d8;background:#eef0f0}
.search-field{flex:1;font-size:7px;color:#999;padding:5px 4px}
.search-btn{width:18px;background:var(--green)}

.main-nav{position:absolute;left:0;top:107px;width:1056px;height:39px;background:var(--green);font-family:"Mulish",sans-serif}
.main-nav a{position:absolute;top:12px;font-size:12px;color:#fff;letter-spacing:.2px}

.hero{position:absolute;left:0;top:146px;width:1056px;height:430px;
  background:linear-gradient(100deg,#8a6a55 0%,#a88470 30%,#b9907e 50%,#6b4636 68%,#c9a08a 80%,#d8c3b2 100%)}
.welcome{position:absolute;left:88px;top:227px;width:356px;height:220px;background:rgba(255,255,255,.2);color:#fff;padding:24px 30px}
.welcome h1{font-family:"Mulish",sans-serif;font-weight:400;font-size:24px;line-height:1.1;margin-bottom:18px}
.welcome p{font-size:13.5px;line-height:17.4px}
.welcome .more{position:absolute;right:30px;bottom:16px;font-size:13.5px;color:#2b2b2b}

.panel{position:absolute;left:86px;top:526px;width:884px;height:634px;background:var(--white);border-radius:10px 10px 0 0}
.tab{position:absolute;top:538px;width:221px;height:38px;color:#fff;font-family:"Mulish",sans-serif;font-size:15px;padding:10px 18px}
.tab-news{left:86px;background:var(--yellow)}
.tab-learn{left:307px;background:var(--red);padding-left:21px}
.tab-reg{left:528px;background:var(--teal)}
.tab-sched{left:749px;background:var(--green)}

.news{position:absolute;left:103px;top:604px;width:196px}
.news-item{margin-bottom:9px}
.news-date{font-size:13px;line-height:16.5px;color:#333;margin-bottom:4px}
.news-link{font-size:13px;line-height:16.3px;color:var(--gold-link)}

.thumb{position:absolute;top:606px;width:183px;height:80px}
.thumb-learn{left:325px;background:linear-gradient(90deg,#3b2723,#c49b8a 40%,#e9d2c5 60%,#503730)}
.thumb-reg{left:546px;background:linear-gradient(90deg,#e8eef2,#caa390 35%,#e9e4e0 60%,#ffffff 78%,#8e969b 92%,#e6e9ea)}
.col-text{position:absolute;top:703px;width:192px;font-size:12.8px;line-height:16.2px;color:#333}
.col-learn{left:325px}
.col-reg{left:544px}
.col-reg p+p{margin-top:16px}
.link-red{color:var(--red)}
.link-teal{color:var(--teal)}

.schedule{position:absolute;left:764px;top:602px;width:196px;list-style:none}
.schedule li{position:relative;padding-left:13px;font-size:12.8px;line-height:16.2px;color:var(--green)}
.schedule li::before{content:"";position:absolute;left:1px;top:6px;width:4px;height:4px;background:#555}

.divider{position:absolute;left:106px;top:917px;width:842px;height:1px;background:#e3e3e3}
.section-title{position:absolute;top:946px;font-family:"Mulish",sans-serif;font-size:15.5px;font-weight:400;color:#333}
.why-text{position:absolute;left:107px;top:982px;width:396px;font-size:12.8px;line-height:16.2px;color:#333}
.link-green{color:var(--green)}

.field{position:absolute;left:536px;width:182px;height:31px;background:var(--field);font-size:12.5px;font-style:italic;color:#aaa;padding:7px 15px}
.register{position:absolute;left:536px;top:1067px;width:101px;height:30px;background:var(--green);color:#fff;font-size:12.8px;padding:6px 16px}

.contact{position:absolute;left:752px;top:980px;width:210px;font-size:12px;line-height:15.2px;font-style:italic;color:#444}
.contact .mail{color:var(--green)}
.contact .maps{margin-top:15px;color:var(--green)}

.footer-copy{position:absolute;left:93px;top:1178px;font-size:8.5px;color:var(--muted)}
.footer-links{position:absolute;top:1178px;font-size:8.5px;color:var(--muted)}
.social{position:absolute;top:1169px;width:24px;height:24px;border-radius:50%;background:#d6d8d8}
</style>
</head>
<body>

<header class="site-header">
  <div class="brand"><span class="brand-mark"></span><span class="brand-name">Brisk Lyceum</span></div>
  <a class="login" href="#">Login</a>
  <div class="search"><span class="search-drop"></span><span class="search-field">Search</span><span class="search-btn"></span></div>
</header>

<nav class="main-nav">
  <a style="left:112px" href="#">HOME</a>
  <a style="left:188px" href="#">ABOUT US</a>
  <a style="left:289px" href="#">MATHS</a>
  <a style="left:371px" href="#">PHYSICS</a>
  <a style="left:460px" href="#">CHEMISTRY</a>
  <a style="left:568px" href="#">BIOLOGY</a>
  <a style="left:659px" href="#">SCIENCE FAIR</a>
  <a style="left:786px" href="#">FALL 2013</a>
  <a style="left:881px" href="#">RESULTS</a>
</nav>

<section class="hero" role="img" aria-label="Photo of a smiling student with glasses outdoors on a campus"></section>
<div class="welcome">
  <h1>Welcome to Brisk Lyceum</h1>
  <p>Welcome to Brisk Lyceum for Gifted Youth. We provide after-school enrichment programs in math, physics, chemistry, biology, and computer science, mentor middle and high school science research projects, and offer college counseling to aspiring students in pursuing their college dream</p>
  <a class="more" href="#">...read more</a>
</div>

<div class="panel"></div>
<div class="tab tab-news">News &amp; Events</div>
<div class="tab tab-learn">E-learning</div>
<div class="tab tab-reg">Registration</div>
<div class="tab tab-sched">Scheduler</div>

<div class="news">
  <div class="news-item"><div class="news-date">February 12th 2013</div><a class="news-link" href="#">Lorem ipsum dolor sep sit aet sed lorem ipsum onectur...</a></div>
  <div class="news-item"><div class="news-date">February 12th 2013</div><a class="news-link" href="#">Lorem ipsum dolor sep sit aet sed lorem ipsum onectur aispicing lipe consectetur...</a></div>
  <div class="news-item"><div class="news-date">February 12th 2013</div><a class="news-link" href="#">Lorem ipsum dolor sep sit aet sed lorem ipsum onectur aispicing lipe consectetur...</a></div>
  <div class="news-item"><div class="news-date">February 12th 2013</div><a class="news-link" href="#">Lorem ipsum dolor sep sit aet sed lorem ipsum onectur...</a></div>
</div>

<div class="thumb thumb-learn" role="img" aria-label="Photo of two students studying together at a laptop"></div>
<div class="col-text col-learn">Students have access to learning resources, can review classroom materials, download homework solutions, view grade reports, and share knowledge with classmates in a protected environment. Parents will be able to monitor their children's learning progress and participate in forum discussions related to development. <a class="link-red" href="#">Click here</a> to log in</div>

<div class="thumb thumb-reg" role="img" aria-label="Photo of a student resting her head on a stack of books"></div>
<div class="col-text col-reg">
  <p>The early registration deadline for returning students and summer camp participants is August 15. The open registration period is from August 15, 2013 - August 31, 2013.&nbsp; To register, clink on the program title below</p>
  <p>To learn more about class schedule, qualification, waiting list, and other information <a class="link-teal" href="#">click here.</a></p>
</div>

<ul class="schedule">
  <li>Math Olympiad Classes</li>
  <li>Physics, Chemistry, Computer Science, and Biology Olympiad Classes</li>
  <li>Fall Session: September 10, 2013 - November 17, 2013</li>
  <li>Winter Session: Dec 3, 2013-Feb 23, 2013 (Holiday Break from Dec 23, 2013 - Jan 5, 2014)</li>
  <li>Winter Olympiads Bootcamp:Dec 26 - 30, 2013</li>
  <li>Spring Session: Mar 3, 2014 - May 11, 2014</li>
  <li>Jump Start Math Classes</li>
  <li>Biology Olympiad Summer Camp</li>
  <li>Student Registration : Schedule a qualifying exam</li>
</ul>

<div class="divider"></div>

<h2 class="section-title" style="left:107px">Why Brisk Lyceum for Gifted Youth?</h2>
<p class="why-text">In 2006, Brisk Lyceum for Gifted Youth was the first academy to offer advanced math problem solving to gifted students in Orange County. With its roots in the Irvine math community and locations proximate to Harborview State University and Lakemont University, Brisk Lyceum for Gifted Youth combines California Standardized Mathematics Curriculum with math competitions and problem solving to help gifted students to discover their passion, develop their skills, and fulfill their college dreams.&nbsp; To learn more about our philosophy, history, statement of differentiation, and approach to gifted education, <a class="link-green" href="#">click here.</a></p>

<h2 class="section-title" style="left:535px">Newsletter</h2>
<div class="field" style="top:985px">Name</div>
<div class="field" style="top:1026px">Email</div>
<a class="register" href="#">Register me</a>

<h2 class="section-title" style="left:751px">Contact us</h2>
<address class="contact">
  Brisk Lyceum for Gifted Youth<br>
  2750 Quarry Lane, Suite 140<br>
  Irvine, CA 92600-0000<br>
  Phone: (555) 014-2211<br>
  Fax:&nbsp;&nbsp;&nbsp;&nbsp;(555) 014-0888<br>
  e-mail: <span class="mail">info@brisklyceum-example.com</span>
  <div class="maps">Maps to Brisk Lyceum, Irvine<br>Directions to Brisk Lyceum, Irvine</div>
</address>

<div class="footer-copy">2013 Brisk Lyceum&nbsp; All Right Reserved</div>
<a class="footer-links" style="left:661px" href="#">FAQs</a>
<a class="footer-links" style="left:697px" href="#">Terms Of Use</a>
<a class="footer-links" style="left:764px" href="#">Privacy Policy</a>
<a class="footer-links" style="left:835px" href="#">Careers</a>
<span class="social" style="left:883px"></span>
<span class="social" style="left:915px"></span>
<span class="social" style="left:945px"></span>

</body>
</html>
```